Design Challege - Simplify a Complex Message

We have a new website design, but one of the pages presents a particular problem.

Our company does ERP implementations. We have developed a proprietary approach to these implementations based on the idea that you must get eight (and only eight) things right. These eight things are listed below, summarized in one or two words each:

1. Value
2. Capability
3. Functionality
4. Data
5. Technology
6. Change Leadership
7. Quality
8. Governance

Each of these eight things can be summarized in a short paragraph, but when you combine all eight summaries with a brief introductory text, the result is a lot of text - so much text that the casual surfer may be overwhelmed by it.

The winning design will find an engaging way to present the information in a way that presents a high-level summary, using icons and one- or two-word descriptions above but revealing more information when clicked.

Our current design for this information, with a paragraph describing the eight elements in a table, is included as an upload in PDF and Microsoft Word formats. We are looking for a creative way to display these eight things, showing the detail only when the user wants to see it.

The website is being built in WordPress, using Elementor as a page builder.

We will implement (code) the page, but the winner will be asked to specify the widget or other add-in if one is required.

The design does not need to include a header or footer, we have those.

Target Market(s)

Business executives working in technology

Industry/Entity Type

Any

Number of Pages Required

1 page

Font styles to use
Sans Serif

Requirements
Must have
• A design for the body of the page, but not the header or footer.
Nice to have
• Unique icons or images appropriate for each of the eight things.
Should not have
• A lot of text on one page

```html
<!DOCTYPE html>
<html lang="en">
<head>
<meta charset="utf-8">
<title>ERP Implementations – Eight Things to Get Right</title>
<link href="https://fonts.googleapis.com/css2?family=Playfair+Display:wght@700&family=Open+Sans:wght@400;600;700&display=swap" rel="stylesheet">
<style>
  :root{
    --blue:#1a86c8;
    --blue-light:#4fb0e3;
    --blue-deep:#0b5a97;
    --navy:#0d4a7e;
    --ink:#1b2330;
    --body:#6d7480;
    --grey-band:#eceff2;
    --white:#ffffff;
  }
  *{box-sizing:border-box;margin:0;padding:0}
  html,body{width:1200px;height:4144px;overflow:hidden;background:var(--white)}
  body{font-family:"Open Sans",Arial,sans-serif;color:var(--body)}

  .hero{position:relative;height:300px;text-align:center;color:var(--white);
    background:linear-gradient(180deg,#2a9ad8 0%,#1b86c9 100%)}
  .hero-wave{position:absolute;left:0;bottom:0;width:1200px;height:60px}
  .hero-title{position:relative;padding-top:32px;font-family:"Playfair Display",Georgia,serif;font-size:50px;line-height:54px;font-weight:700}
  .hero-subtitle{position:relative;margin-top:8px;font-size:24px;font-weight:400}
  .hero-intro{position:relative;width:560px;margin:10px auto 0;font-size:12px;line-height:18px;opacity:.92}
  .hero-toggle{position:absolute;left:584px;top:236px;width:32px;height:32px;border-radius:50%;
    background:var(--white);z-index:2;display:flex;align-items:center;justify-content:center;
    box-shadow:0 2px 6px rgba(0,0,0,.15)}

  .feature{position:relative;display:flex;align-items:center;justify-content:center;gap:100px;padding:0 140px}
  .feature--plain{background:var(--white)}
  .feature--grey{background:var(--grey-band)}
  .feature--blue{background:linear-gradient(135deg,#58b6e6 0%,#3c9fd9 100%)}
  .feature--reverse .feature-media{order:-1}

  .feature-copy{width:420px}
  .feature-title{font-family:"Playfair Display",Georgia,serif;font-size:34px;line-height:40px;font-weight:700;color:var(--ink);margin-bottom:16px}
  .feature-text{font-size:12px;line-height:19px;color:var(--body)}
  .feature-list{list-style:none;margin-top:10px}
  .feature-list li{position:relative;padding-left:20px;font-size:12px;line-height:22px}
  .feature-list li::before{content:"";position:absolute;left:0;top:6px;width:10px;height:10px;border-radius:2px;background:var(--blue)}
  .feature--blue .feature-title,.feature--blue .feature-text{color:var(--white)}

  .learn-more{display:inline-block;margin-top:20px;padding:0 20px;height:30px;line-height:30px;border-radius:15px;
    background:var(--navy);color:var(--white);font-size:10px;font-weight:700;letter-spacing:.6px;text-decoration:none}
  .feature--blue .learn-more{background:transparent;border:1.5px solid var(--white)}

  .feature-media{position:relative;width:420px;height:420px;flex:none}
  .photo{position:absolute;inset:10px;border-radius:50%}
  .badge{position:absolute;width:150px;height:150px;border-radius:50%;background:var(--blue);
    border:6px solid var(--white);display:flex;align-items:center;justify-content:center;
    box-shadow:0 6px 18px rgba(0,0,0,.15)}
  .badge--left{left:-20px;bottom:50px}
  .badge--right{right:-20px;bottom:50px}
  .badge svg{width:70px;height:70px;fill:none;stroke:var(--white);stroke-width:3;stroke-linecap:round;stroke-linejoin:round}
</style>
</head>
<body>

<header class="hero">
  <h1 class="hero-title">ERP<br>Implementations</h1>
  <p class="hero-subtitle">Eight Things to Get Right</p>
  <p class="hero-intro">In an ERP implementation, you must get eight major things right to be successful. Miss any of them, and your implementation will fail. Get them right, and you will likely succeed.</p>
  <span class="hero-toggle"><svg width="14" height="14" viewBox="0 0 14 14"><path d="M7 1v12M1 7h12" stroke="#1a86c8" stroke-width="2.4" stroke-linecap="round"/></svg></span>
  <svg class="hero-wave" viewBox="0 0 1200 60" preserveAspectRatio="none"><path d="M0 60 C300 0 900 0 1200 60 Z" fill="#ffffff"/></svg>
</header>

<section class="feature feature--plain" style="height:520px">
  <div class="feature-copy">
    <h2 class="feature-title">Value</h2>
    <p class="feature-text">The project must provide value that significantly exceeds potential project costs and should be aligned with the company's strategy. Be sure your strategic alignment would be part of a vision shared by the company's leadership. Value from the project must be delivered in a way that requires minimal investment.</p>
    <a class="learn-more" href="#">LEARN MORE</a>
  </div>
  <div class="feature-media">
    <div class="photo" role="img" aria-label="Hand stacking wooden blocks into rising steps with a red arrow" style="background:radial-gradient(circle at 40% 40%,#e9e4dc,#c9a47a 70%,#8a6a48)"></div>
    <div class="badge badge--left"><svg viewBox="0 0 70 70"><circle cx="24" cy="40" r="14"/><path d="M24 33v14M20 36h7M20 44h7"/><path d="M46 56V26M38 34l8-8 8 8"/></svg></div>
  </div>
</section>

<section class="feature feature--grey feature--reverse" style="height:520px">
  <div class="feature-copy">
    <h2 class="feature-title">Capability</h2>
    <p class="feature-text">The company and the implementation team must be capable of implementing the project as they plan it with help. The system must have the following:</p>
    <ul class="feature-list">
      <li>Resourced capacity including people, time and budget</li>
      <li>Processes mapped, clearly delivered through a comprehensive roadmap</li>
      <li>Prioritization backed because an ERP project will need the commitment of the entire company</li>
    </ul>
    <a class="learn-more" href="#">LEARN MORE</a>
  </div>
  <div class="feature-media">
    <div class="photo" role="img" aria-label="Hand reaching toward glowing digital gears" style="background:radial-gradient(circle at 55% 45%,#f3c7b6,#5aa9d6 55%,#1e5d93)"></div>
    <div class="badge badge--right"><svg viewBox="0 0 70 70"><circle cx="35" cy="35" r="9"/><path d="M35 12v8M35 50v8M12 35h8M50 35h8M19 19l6 6M45 45l6 6M19 51l6-6M45 25l6-6"/></svg></div>
  </div>
</section>

<section class="feature feature--plain" style="height:380px">
  <div class="feature-copy">
    <h2 class="feature-title">Functionality</h2>
    <p class="feature-text">An ERP system must support required business processes both now and in the future. A systematic review of all business processes and how they will be supported, either by the system or effectively in a layer.</p>
    <a class="learn-more" href="#">LEARN MORE</a>
  </div>
  <div class="feature-media" style="width:360px;height:360px">
    <div class="photo" role="img" aria-label="Hand touching a ring of glowing function icons" style="background:radial-gradient(circle at 50% 50%,#4d86c4,#16355f 60%,#0b1a33)"></div>
    <div class="badge badge--left" style="bottom:30px"><svg viewBox="0 0 70 70"><circle cx="28" cy="30" r="8"/><path d="M28 14v6M28 40v6M12 30h6M38 30h6"/><circle cx="48" cy="50" r="6"/><path d="M48 38v4M48 58v4M36 50h4M56 50h4"/></svg></div>
  </div>
</section>

<section class="feature feature--blue feature--reverse" style="height:460px">
  <div class="feature-copy">
    <h2 class="feature-title">Data</h2>
    <p class="feature-text">ERP systems are data-hungry machines. Processes and functions depending on that data may be made visible and reflected as useful decisions on shared information. Making major data decisions demands careful planning and architecture, migration, integration, governance, and proper cleanup and quality control.</p>
    <a class="learn-more" href="#">LEARN MORE</a>
  </div>
  <div class="feature-media" style="width:380px;height:380px">
    <div class="photo" role="img" aria-label="Hand holding a glowing cloud of connected data" style="background:radial-gradient(circle at 50% 45%,#bfe6ff,#2f82c4 55%,#0e3a6e)"></div>
    <div class="badge badge--right" style="bottom:40px"><svg viewBox="0 0 70 70"><ellipse cx="35" cy="18" rx="18" ry="6"/><path d="M17 18v34c0 3.3 8 6 18 6s18-2.7 18-6V18M17 30c0 3.3 8 6 18 6s18-2.7 18-6M17 41c0 3.3 8 6 18 6s18-2.7 18-6"/></svg></div>
  </div>
</section>

<section class="feature feature--plain" style="height:480px">
  <div class="feature-copy">
    <h2 class="feature-title">Technology</h2>
    <p class="feature-text">What is the platform for the system? Is it offered by a vendor that will be around for as long as your system? Will it integrate with your other systems? Are resources available to support it? Can you change it without spending yourself into a corner? Are your technology costs fair as you grow?</p>
    <a class="learn-more" href="#">LEARN MORE</a>
  </div>
  <div class="feature-media" style="width:400px;height:400px">
    <div class="photo" role="img" aria-label="Glowing light bulb made of circuit lines on dark blue" style="background:radial-gradient(circle at 50% 45%,#6fd0ff,#1456a0 45%,#061a3a)"></div>
    <div class="badge badge--left" style="bottom:40px"><svg viewBox="0 0 70 70"><path d="M26 46c-6-4-10-10-10-17a19 19 0 0 1 38 0c0 7-4 13-10 17v6H26z"/><path d="M28 58h14"/><circle cx="35" cy="29" r="6"/></svg></div>
  </div>
</section>

<section class="feature feature--grey feature--reverse" style="height:520px">
  <div class="feature-copy">
    <h2 class="feature-title">Change Leadership</h2>
    <p class="feature-text">Change leadership (often called change management) considers the human side of an ERP implementation. Change is hard, even if it's a good change. Training is an important element of change leadership, but beyond training, consideration must be given to the people using the system. How are they involved in communication and important decisions? What will motivate them to make the implementation a success?</p>
    <a class="learn-more" href="#">LEARN MORE</a>
  </div>
  <div class="feature-media">
    <div class="photo" role="img" aria-label="Team of business people standing together in an office" style="background:radial-gradient(circle at 50% 40%,#e6e8ec,#9aa3ad 60%,#3b4450)"></div>
    <div class="badge badge--left"><svg viewBox="0 0 70 70"><circle cx="35" cy="22" r="7"/><path d="M24 52V40a11 11 0 0 1 22 0v12"/><circle cx="16" cy="30" r="5"/><path d="M8 52v-8a8 8 0 0 1 12-7"/><circle cx="54" cy="30" r="5"/><path d="M62 52v-8a8 8 0 0 0-12-7"/></svg></div>
  </div>
</section>

<section class="feature feature--plain" style="height:480px">
  <div class="feature-copy">
    <h2 class="feature-title">Quality</h2>
    <p class="feature-text">Quality is multi-dimensional, and the most basic is independence of a perception. An ERP needs to be reliable. But poor performance in your core experience can often end in a complex implementation failure. Take an approach to quality that starts with perceptions and considers all aspects of quality.</p>
    <a class="learn-more" href="#">LEARN MORE</a>
  </div>
  <div class="feature-media" style="width:400px;height:400px">
    <div class="photo" role="img" aria-label="Open hands presenting a glowing shield symbol" style="background:radial-gradient(circle at 50% 40%,#d9ecf7,#47657f 55%,#121d29)"></div>
    <div class="badge badge--left" style="bottom:40px"><svg viewBox="0 0 70 70"><path d="M35 10l20 8v14c0 13-9 22-20 27-11-5-20-14-20-27V18z"/><path d="M26 34l6 6 12-12"/></svg></div>
  </div>
</section>

<section class="feature feature--blue feature--reverse" style="height:484px">
  <div class="feature-copy">
    <h2 class="feature-title">Governance</h2>
    <p class="feature-text">ERP projects require both management and leadership. Planning, change policy, communication, decision making, and governance enable aspects of management. The process of incorporating guidance or instituting a team, steering the goals, and being consistent to ensure goals meet well-managed guidance is vital.</p>
    <a class="learn-more" href="#">LEARN MORE</a>
  </div>
  <div class="feature-media">
    <div class="photo" role="img" aria-label="Business people meeting around a table" style="background:radial-gradient(circle at 50% 45%,#f0e6da,#9fb6c8 55%,#385a78)"></div>
    <div class="badge badge--right"><svg viewBox="0 0 70 70"><path d="M12 26L35 12l23 14z"/><path d="M14 26h42M18 30v20M29 30v20M41 30v20M52 30v20M12 54h46M10 58h50"/></svg></div>
  </div>
</section>

</body>
</html>
```